Labels designs for a new coffee brand (Vestro Coffee)

We looking for a coffee label design for our coffee Brand, VESTRO COFFE, attached is the logo. We are bringing out to the market 3 Premium blends
1. Colombian Popayan
2. Gourmet Expresso Blend
3. Brazilian Santos

We like something that looks high quality yet modern, the bags we are using is black matte, we are starting with labels and look in the near future to print our own labels .

We want the labels for the 3 coffees to have the similar look and feel but to be uniquely identified by its design (Colombian, Brazilian, espresso) This is beig sold as a set so we want it to have a similar label feeling but that each is identify as its unique product (colombian, expresso, brazilian blend.

This project is for labels that will be used on a black matte bag, is for a 16 oz bag,

Attached is a sample of the bag color.

Size Requirements:
Maintain a 2:3 aspect ratio for the image file
The label will be 4" wide and 6" tall (we also want to print some 3X4)
Recommended image size is 1600px X 2400px

I will provide upc later

www.vestrocoffee.example pw 48071 this is the test site not live yet but you can get a feel of the brand
Updates

Ay my daughters volleyball tournament I need extra time to review

Target Market(s)

coffee drinkers

Industry/Entity Type

coffee

Requirements
Must have
• Creativity, unique, eye catchy,

```html
<!DOCTYPE html>
<html lang="en">
<head>
<meta charset="utf-8">
<title>Vestro Coffee — Label Set</title>
<link rel="stylesheet" href="https://fonts.googleapis.com/css2?family=Baloo+2:wght@600;700;800&family=Josefin+Sans:wght@400;600;700&family=Roboto:wght@400&display=swap">
<style>
  :root {
    --canvas: #f3f1ee;
    --paper: #f7f1ea;
    --paper-stain: rgba(214, 170, 135, 0.35);
    --brown: #8c5a3a;
    --ink: #1f1a17;
    --panel: #dcd7ca;
    --panel-line: #5a534c;
    --stamp: #c8203a;
    --santos-a: #d8471a;
    --santos-b: #b3221a;
    --popayan-a: #c8102e;
    --popayan-b: #9d0f30;
    --espresso-a: #0c8a62;
    --espresso-b: #07604a;
  }
  * { box-sizing: border-box; margin: 0; padding: 0; }
  html, body { width: 1200px; height: 873px; overflow: hidden; background: var(--canvas); }
  .label-set {
    width: 1200px; height: 873px;
    display: flex; justify-content: center; align-items: center; gap: 44px;
  }
  .label {
    --accent-a: var(--santos-a);
    --accent-b: var(--santos-b);
    position: relative; width: 340px; height: 560px;
    border-radius: 14px; overflow: hidden;
    background:
      radial-gradient(ellipse 60% 30% at 10% 5%, var(--paper-stain), transparent 70%),
      radial-gradient(ellipse 50% 25% at 95% 40%, rgba(214,170,135,.2), transparent 70%),
      radial-gradient(ellipse 70% 30% at 20% 85%, rgba(214,170,135,.25), transparent 70%),
      var(--paper);
    box-shadow: 0 10px 30px rgba(0,0,0,.12);
    font-family: "Josefin Sans", sans-serif;
  }
  .label--popayan { --accent-a: var(--popayan-a); --accent-b: var(--popayan-b); }
  .label--espresso { --accent-a: var(--espresso-a); --accent-b: var(--espresso-b); }

  .roast-arc { position: absolute; top: 34px; left: 0; width: 340px; height: 70px; }
  .roast-arc text { font-family: "Josefin Sans", sans-serif; fill: var(--brown); font-weight: 700; }

  .brand {
    position: absolute; top: 165px; left: 0; right: 0;
    display: flex; justify-content: center; align-items: center; gap: 12px;
    transform: rotate(-2deg);
  }
  .brand-dot { width: 22px; height: 22px; border-radius: 50%; background: var(--brown); }
  .brand-name {
    font-family: "Josefin Sans", sans-serif; font-weight: 600;
    font-size: 54px; letter-spacing: 4px; color: var(--brown); line-height: 1;
  }

  .product-name {
    position: absolute; top: 282px; left: 0; right: 0; text-align: center;
    font-family: "Baloo 2", sans-serif; font-weight: 800;
    font-size: 27px; line-height: .95; color: var(--accent-a);
    transform: rotate(-3deg);
  }

  .info-panel {
    position: absolute; top: 362px; left: 28px; width: 284px; height: 138px;
    background: var(--panel); transform: rotate(-3deg);
    display: grid; grid-template-columns: 134px 1fr;
    padding: 10px 10px 16px;
  }
  .info-panel::before, .info-panel::after {
    content: ""; position: absolute; left: 0; right: 0; height: 6px;
    background:
      linear-gradient(-45deg, transparent 4px, var(--panel) 0),
      linear-gradient(45deg, transparent 4px, var(--panel) 0);
    background-size: 8px 8px;
  }
  .info-panel::before { top: -6px; transform: rotate(180deg); }
  .info-panel::after { bottom: -6px; }
  .stitch {
    position: absolute; left: 4px; right: 4px; bottom: 4px; height: 4px;
    background:
      linear-gradient(-45deg, transparent 2px, var(--panel-line) 0 3px, transparent 0),
      linear-gradient(45deg, transparent 2px, var(--panel-line) 0 3px, transparent 0);
    background-size: 6px 4px; opacity: .6;
  }
  .info-origin { border-right: 1px solid var(--panel-line); padding-right: 8px; }
  .origin-name {
    font-family: "Baloo 2", sans-serif; font-weight: 700; font-size: 20px;
    color: var(--ink); line-height: 1; padding: 12px 0 7px;
    border-bottom: 1px solid var(--panel-line);
  }
  .grind {
    font-family: "Baloo 2", sans-serif; font-weight: 700; font-size: 12px;
    line-height: 1; color: var(--ink); text-align: center; margin: 6px 0 0 30px;
  }
  .quality-stamp {
    width: 48px; height: 48px; border-radius: 50%;
    border: 1.5px solid var(--stamp); margin: -6px 0 0 0;
  }
  .info-specs { padding-left: 10px; color: var(--ink); }
  .grind-alt {
    font-family: "Baloo 2", sans-serif; font-weight: 700; font-size: 9.5px;
    line-height: 1; text-align: center; padding-bottom: 5px;
    border-bottom: 1px solid var(--panel-line);
  }
  .spec-row {
    display: flex; justify-content: space-between; padding: 8px 4px 10px;
    border-bottom: 1px solid var(--panel-line);
  }
  .spec strong { display: block; font-family: "Baloo 2", sans-serif; font-weight: 700; font-size: 12px; line-height: 1; }
  .spec span { display: block; font-family: "Roboto", sans-serif; font-size: 8px; line-height: 1.1; }
  .organic {
    text-align: center; font-weight: 700; font-size: 9px; letter-spacing: 1.8px; padding-top: 10px;
  }

  .web-band {
    position: absolute; left: 0; right: 0; bottom: 0; height: 100px;
    background: linear-gradient(90deg, var(--accent-a), var(--accent-b));
    clip-path: polygon(0 48%, 100% 0, 100% 100%, 0 100%);
  }
  .web-address {
    position: absolute; left: 0; right: 0; bottom: 26px; text-align: center;
    color: #fff; font-weight: 700; font-size: 12px; letter-spacing: 2px;
    transform: rotate(-8deg);
  }
</style>
</head>
<body>
<main class="label-set">

  <article class="label label--santos">
    <svg class="roast-arc" viewBox="0 0 340 70" aria-hidden="false">
      <path id="arc-santos" d="M70 48 Q170 18 270 48" fill="none"/>
      <text font-size="11" letter-spacing="2"><textPath href="#arc-santos" startOffset="50%" text-anchor="middle">- SMALL-BATCH ROASTED -</textPath></text>
      <text x="170" y="50" font-size="8" text-anchor="middle" letter-spacing="0.5">· EST. 2023 ·</text>
    </svg>
    <div class="brand"><span class="brand-dot"></span><span class="brand-name">VESTRO</span></div>
    <h2 class="product-name">BRAZILEAN<br>SANTOS</h2>
    <section class="info-panel">
      <div class="info-origin">
        <div class="origin-name">COLOMBIAN</div>
        <div class="grind">REGULAR<br>GROUND</div>
        <div class="quality-stamp"></div>
      </div>
      <div class="info-specs">
        <div class="grind-alt">WHOLE<br>BEAM</div>
        <div class="spec-row">
          <div class="spec"><strong>100%</strong><span>Cafe Arabica</span></div>
          <div class="spec"><strong>12 Oz</strong><span>340 gr</span></div>
        </div>
        <div class="organic">ORGANIC BEANS</div>
      </div>
      <span class="stitch"></span>
    </section>
    <div class="web-band"></div>
    <p class="web-address">VESTROCOFFEE.EXAMPLE</p>
  </article>

  <article class="label label--popayan">
    <svg class="roast-arc" viewBox="0 0 340 70">
      <path id="arc-popayan" d="M70 48 Q170 18 270 48" fill="none"/>
      <text font-size="11" letter-spacing="2"><textPath href="#arc-popayan" startOffset="50%" text-anchor="middle">- SMALL-BATCH ROASTED -</textPath></text>
      <text x="170" y="50" font-size="8" text-anchor="middle" letter-spacing="0.5">· EST. 2023 ·</text>
    </svg>
    <div class="brand"><span class="brand-dot"></span><span class="brand-name">VESTRO</span></div>
    <h2 class="product-name">COLOMBIAN<br>POPAYAN</h2>
    <section class="info-panel">
      <div class="info-origin">
        <div class="origin-name">COLOMBIAN</div>
        <div class="grind">REGULAR<br>GROUND</div>
        <div class="quality-stamp"></div>
      </div>
      <div class="info-specs">
        <div class="grind-alt">WHOLE<br>BEAM</div>
        <div class="spec-row">
          <div class="spec"><strong>100%</strong><span>Cafe Arabica</span></div>
          <div class="spec"><strong>12 Oz</strong><span>340 gr</span></div>
        </div>
        <div class="organic">ORGANIC BEANS</div>
      </div>
      <span class="stitch"></span>
    </section>
    <div class="web-band"></div>
    <p class="web-address">VESTROCOFFEE.EXAMPLE</p>
  </article>

  <article class="label label--espresso">
    <svg class="roast-arc" viewBox="0 0 340 70">
      <path id="arc-espresso" d="M70 48 Q170 18 270 48" fill="none"/>
      <text font-size="11" letter-spacing="2"><textPath href="#arc-espresso" startOffset="50%" text-anchor="middle">- SMALL-BATCH ROASTED -</textPath></text>
      <text x="170" y="50" font-size="8" text-anchor="middle" letter-spacing="0.5">· EST. 2023 ·</text>
    </svg>
    <div class="brand"><span class="brand-dot"></span><span class="brand-name">VESTRO</span></div>
    <h2 class="product-name">GOURMET EXPRESSO<br>BLEND</h2>
    <section class="info-panel">
      <div class="info-origin">
        <div class="origin-name">COLOMBIAN</div>
        <div class="grind">REGULAR<br>GROUND</div>
        <div class="quality-stamp"></div>
      </div>
      <div class="info-specs">
        <div class="grind-alt">WHOLE<br>BEAM</div>
        <div class="spec-row">
          <div class="spec"><strong>100%</strong><span>Cafe Arabica</span></div>
          <div class="spec"><strong>12 Oz</strong><span>340 gr</span></div>
        </div>
        <div class="organic">ORGANIC BEANS</div>
      </div>
      <span class="stitch"></span>
    </section>
    <div class="web-band"></div>
    <p class="web-address">VESTROCOFFEE.EXAMPLE</p>
  </article>

</main>
</body>
</html>
```